Perfume Oil manufacturing and distribution company needs an emotion inspiring Wordpress Design

Must be Wordpress Design
Beautiful website needed for a company that manufactures and distributes scents that fragrance products from fine fragrances to personal care and household products. Please refer to attached file (namely "brief" for detailed explanation of our company, product and design requirements)

Website must be beautiful, and not too cluttered.

Must be coded for use in WordPress after design phase

remember not to flood website with pictures of perfumes and perfume bottles, this website is meant to inspire emotion...looking at the big fragrance brands (Valtorne and Merostel) one will not see pictures of perfume bottles etc. The site is all about emotion and smell and the senses.
Keep this in mind when submitting designs.

The site must captivate and inspire emotion with beautiful visuals.

the website must be about how one feels when surrounded by a beautiful smell, how one feels confident wearing a good scent. how freshly baked break reminds you of your grandmas house, or how a scent can remind of a seductive encounter, or a memory of fun times with friends out on the town, or as simple as the smell of a good cup of coffee or a rose to inspire a new days happenings.

all this emotion and feeling must be tied into the fact that Aroma Forge makes these moments through great smells. Which we supply to manufacturers of these great end products. whether it is a fine fragrance, a lotion, a car fragrance or a home spray. We scent the world around us.

try not to look too much at our existing website as this is outdated and the company has changed much since then, refer to this and the attached brief

Target Market(s)

small to medium businesses who manufacture products that need to be fragranced. whether these products be prestigious fine fragrances, daily personal care products or home care products, we make the fragrances that make these products beautiful.

Industry/Entity Type

Perfume

Coding

Coded - Design and coding required

Number of Pages Required

5+ page

Font styles to use
Serif
Sans Serif

Colors

Designer to choose colors to be used in the design.

Requirements
Must have
• must have full page header that captivates audience and inspires emotion (through a video or powerful imagery)
• Smell is a powerful emotion trigger and since a computer screen can not produce smell we will need to engage emotion through beautiful imagery and or video and beautiful design on the website. (refer to attached "brief" for more details)
• Must be coded for use in WordPress ONLY after design phase
• site must work well and look great on mobile since most of our audience use mobile to access our site.
Should not have
• too many pictures of perfume packaging and actual products, looking at the big fragrance manufacturers (Valtorne, Merostel, KDW) one will not see pictures of perfume bottles and packaging. This is very important as the website is more to inspire emotion and give a sense of how fragrance and perfume makes one feel.
• The site must captivate and inspire emotion with beautiful visuals.

```html
<!DOCTYPE html>
<html lang="en">
<head>
<meta charset="utf-8">
<title>Aroma Forge – Master Perfumers</title>
<link href="https://fonts.googleapis.com/css2?family=Lato:ital,wght@0,300;0,400;0,700;1,400;1,700&family=Righteous&family=Varela+Round&display=swap" rel="stylesheet">
<style>
:root{
  --blue:#2f8fd0;
  --blue-dark:#1f6fa6;
  --ink:#2e2e2e;
  --text:#555;
  --muted:#777;
  --light:#f6f6f6;
  --white:#fff;
  --footer:#343434;
  --footer-bar:#2a2a2a;
  --ring:#cfcfcf;
}
*{margin:0;padding:0;box-sizing:border-box}
html,body{width:1200px;height:3543px;overflow:hidden;background:var(--white)}
body{font-family:"Lato",sans-serif;color:var(--text);position:relative}
.abs{position:absolute}
.center{left:0;width:1200px;text-align:center}
.section-title{font-family:"Righteous",sans-serif;font-weight:400;font-size:46px;color:var(--blue);letter-spacing:1px}
.section-text{font-size:14px;line-height:28px;color:var(--text);width:700px;margin:0 auto}

/* header */
.site-header{top:0;left:0;width:1200px;height:123px;background:var(--white);z-index:5}
.brand{left:74px;top:38px;display:flex;align-items:center;gap:12px}
.brand-dot{width:42px;height:42px;border-radius:50%;background:var(--blue)}
.brand-name{font-family:"Varela Round",sans-serif;font-size:28px;color:var(--blue)}
.main-nav{left:328px;top:58px;display:flex;gap:30px;font-size:15px;color:var(--muted)}
.main-nav .active{color:var(--blue);font-weight:700}

/* hero */
.hero{top:123px;left:0;width:1200px;height:800px;z-index:2}
.hero-title{left:636px;top:122px;font-family:"Varela Round",sans-serif;font-weight:400;font-size:78px;color:var(--blue);line-height:1;white-space:nowrap}
.hero-sub{left:638px;top:218px;font-family:"Lato",sans-serif;font-weight:300;font-size:56px;color:var(--ink);line-height:1;white-space:nowrap}
.hero-text{left:638px;top:300px;width:480px;font-size:12.5px;line-height:25px;font-style:italic;font-weight:700;color:#4a4a4a}
.btn{display:inline-block;background:var(--blue);color:var(--white);border-radius:30px;text-transform:uppercase;font-size:18px;text-align:center}
.hero-btn{left:635px;top:406px;width:166px;height:57px;line-height:57px}

/* values */
.values{top:590px;left:0;width:1200px;height:442px;background:var(--light);z-index:0}
.values-row{top:680px;left:0;width:1200px;height:352px;z-index:3}
.value{width:300px;text-align:center}
.value-badge{margin:0 auto;width:150px;height:150px;border-radius:50%;background:var(--white);border:4px solid var(--ring);display:flex;align-items:center;justify-content:center}
.value-core{width:122px;height:122px;border-radius:50%;background:var(--ink);display:flex;align-items:center;justify-content:center}
.value.featured .value-core{background:var(--blue)}
.value h3{margin-top:14px;font-size:22px;font-weight:400;color:var(--ink)}
.value.featured h3{color:var(--blue)}
.value p{margin-top:10px;font-size:13.5px;line-height:24px;color:var(--text)}
.more{margin-top:12px;display:inline-flex;align-items:center;gap:10px;font-size:13px;color:var(--muted);text-transform:uppercase}
.value.featured .more{color:var(--blue)}

/* about */
.about-title{top:1075px}
.about-text{top:1140px}
.video{left:260px;top:1219px;width:678px;height:364px;background:
  radial-gradient(circle at 25% 40%,#c7577e 0%,rgba(199,87,126,0) 30%),
  radial-gradient(circle at 58% 35%,#8a4a22 0%,rgba(138,74,34,0) 22%),
  radial-gradient(circle at 70% 75%,#a8322a 0%,rgba(168,50,42,0) 28%),
  linear-gradient(160deg,#4a3c3a 0%,#6c5c58 50%,#8d8380 100%)}
.play{left:564px;top:1366px}

/* services */
.services-band{top:1646px;left:0;width:1200px;height:314px;background:
  radial-gradient(circle at 15% 30%,rgba(140,120,200,.45) 0%,rgba(140,120,200,0) 30%),
  radial-gradient(circle at 85% 40%,rgba(140,120,200,.4) 0%,rgba(140,120,200,0) 30%),
  linear-gradient(180deg,#3f7fa8 0%,#2c6a96 100%)}
.services-title{top:1690px;color:var(--white)}
.services-text{top:1752px;color:#eef4f8}
.service-card{top:1845px;width:316px;height:321px;background:var(--white);border:1px solid #ddd;box-shadow:0 2px 6px rgba(0,0,0,.12)}
.service-photo{margin:10px;height:208px}
.service-card h4{margin-top:14px;text-align:center;font-size:18px;font-weight:400;line-height:30px;color:var(--ink)}
.carousel-arrows{top:2190px;left:555px;display:flex;gap:26px}

/* products */
.products{top:2272px;left:0;width:1200px;height:468px;background:var(--light)}
.products-title{top:50px}
.product{top:134px;width:240px;text-align:center}
.product-ring{margin:0 auto;width:208px;height:208px;border-radius:50%;border:5px solid #7cb9de;background:var(--white);display:flex;align-items:center;justify-content:center}
.product.muted .product-ring{border-color:#c9c9c9}
.product-photo{width:176px;height:176px;border-radius:50%;background:radial-gradient(ellipse 30% 42% at 50% 52%,#fdfdfd 0%,#ececec 80%,rgba(255,255,255,0) 100%),radial-gradient(circle at 50% 45%,#ffffff 0%,#f4f4f4 60%,#e6e6e6 100%)}
.product p{margin-top:22px;font-size:18px;color:var(--ink)}

/* newsletter */
.news-title{top:2785px}
.news-text{top:2860px}
.subscribe{left:262px;top:2948px;width:676px;height:64px;border-radius:32px;background:var(--white);box-shadow:0 3px 10px rgba(0,0,0,.12);display:flex;align-items:center}
.subscribe-field{flex:1;display:flex;align-items:center;gap:14px;padding-left:20px;font-size:13px;font-style:italic;color:var(--muted)}
.subscribe-btn{width:158px;height:64px;line-height:64px;border-radius:0 32px 32px 0;font-weight:700;font-size:17px}

/* footer */
.site-footer{top:3075px;left:0;width:1200px;height:397px;background:var(--footer);color:var(--white)}
.footer-title{left:78px;top:54px;font-size:25px;font-weight:700}
.contact-line{left:78px;display:flex;gap:22px;font-size:13px;line-height:24px;color:#e8e8e8}
.social{display:flex;gap:14px;left:78px}
.social span{width:44px;height:44px;border-radius:50%;background:var(--white);display:block}
.field{border-bottom:1px solid #8a8a8a;font-size:13px;font-weight:700;font-style:italic;padding-bottom:14px;color:var(--white)}
.send-btn{left:435px;top:270px;width:198px;height:56px;line-height:56px;font-size:16px}
.footer-bar{top:3472px;left:0;width:1200px;height:71px;background:var(--footer-bar);color:#ddd;font-size:13px;line-height:71px;text-align:center}
.footer-bar b{font-weight:700}
</style>
</head>
<body>

<header class="site-header abs">
  <div class="brand abs"><span class="brand-dot"></span><span class="brand-name">Aroma Forge</span></div>
  <nav class="main-nav abs">
    <span class="active">Home</span><span>Aroma Forge ?</span><span>Our Services</span><span>Our Products</span><span>Blog</span><span>Contact Us</span><span>Online Training</span><span>Careers</span>
  </nav>
</header>

<section class="values abs"></section>

<section class="hero abs">
  <svg class="abs" style="left:0;top:0" width="1200" height="800" viewBox="0 0 1200 800">
    <defs>
      <linearGradient id="heroWood" x1="0" y1="0" x2="1" y2="0">
        <stop offset="0" stop-color="#e6d5c0"/>
        <stop offset=".5" stop-color="#efe3d4"/>
        <stop offset="1" stop-color="#f4ebe0"/>
      </linearGradient>
      <radialGradient id="heroHerb" cx=".12" cy=".3" r=".22">
        <stop offset="0" stop-color="#7d9a5e" stop-opacity=".75"/>
        <stop offset="1" stop-color="#7d9a5e" stop-opacity="0"/>
      </radialGradient>
      <radialGradient id="heroLavender" cx=".27" cy=".22" r=".16">
        <stop offset="0" stop-color="#a496b8" stop-opacity=".7"/>
        <stop offset="1" stop-color="#a496b8" stop-opacity="0"/>
      </radialGradient>
      <radialGradient id="heroMarigold" cx=".42" cy=".22" r=".16">
        <stop offset="0" stop-color="#e9a23b" stop-opacity=".8"/>
        <stop offset="1" stop-color="#e9a23b" stop-opacity="0"/>
      </radialGradient>
      <radialGradient id="heroOil" cx=".28" cy=".6" r=".22">
        <stop offset="0" stop-color="#e8d9a0" stop-opacity=".8"/>
        <stop offset="1" stop-color="#e8d9a0" stop-opacity="0"/>
      </radialGradient>
      <clipPath id="heroShape"><path d="M0 0H1200V479Q600 777 0 479Z"/></clipPath>
    </defs>
    <g clip-path="url(#heroShape)" role="img" aria-label="Perfume oil bottles with lavender, rosemary and marigold flowers on pale wood">
      <rect width="1200" height="800" fill="url(#heroWood)"/>
      <rect width="1200" height="800" fill="url(#heroHerb)"/>
      <rect width="1200" height="800" fill="url(#heroOil)"/>
      <rect width="1200" height="800" fill="url(#heroLavender)"/>
      <rect width="1200" height="800" fill="url(#heroMarigold)"/>
    </g>
    <path d="M0 479Q600 777 1200 479" fill="none" stroke="#2f8fd0" stroke-width="5"/>
  </svg>
  <h1 class="hero-title abs">Aroma Forge</h1>
  <p class="hero-sub abs">Master Perfumers</p>
  <p class="hero-text abs">Lorem Ipsum is simply dummy text of the printing and typesetting industry. Lorem Ipsum has been the industry's standard dummy text ever since the make a type specimen book.</p>
  <span class="btn hero-btn abs">Learn More</span>
</section>

<div class="values-row abs">
  <div class="value abs" style="left:178px;top:0">
    <div class="value-badge"><div class="value-core">
      <svg width="60" height="60" viewBox="0 0 60 60" fill="#fff"><circle cx="20" cy="14" r="7"/><path d="M10 26h20v14H10z"/><rect x="33" y="22" width="20" height="16" rx="2"/><rect x="6" y="42" width="48" height="5"/></svg>
    </div></div>
    <h3>Legitimacy</h3>
    <p>over 80 years combined<br>experience, industry affiliations<br>with packaging, ethanol.</p>
    <span class="more">Learn More <svg width="20" height="20" viewBox="0 0 20 20"><circle cx="10" cy="10" r="9" fill="none" stroke="#777" stroke-width="1.5"/><path d="M8 6l4 4-4 4" fill="none" stroke="#777" stroke-width="1.5"/></svg></span>
  </div>
  <div class="value featured abs" style="left:450px;top:0">
    <div class="value-badge"><div class="value-core">
      <svg width="60" height="60" viewBox="0 0 60 60" fill="#fff"><circle cx="20" cy="14" r="7"/><path d="M10 26h20v14H10z"/><rect x="33" y="22" width="20" height="16" rx="2"/><rect x="6" y="42" width="48" height="5"/></svg>
    </div></div>
    <h3>Servanthood</h3>
    <p>we are here to serve each<br>stakeholder: customers, suppliers,<br>employees and shareholders.</p>
    <span class="more">Learn More <svg width="20" height="20" viewBox="0 0 20 20"><circle cx="10" cy="10" r="9" fill="none" stroke="#2f8fd0" stroke-width="1.5"/><path d="M8 6l4 4-4 4" fill="none" stroke="#2f8fd0" stroke-width="1.5"/></svg></span>
  </div>
  <div class="value abs" style="left:722px;top:0">
    <div class="value-badge"><div class="value-core">
      <svg width="60" height="60" viewBox="0 0 60 60" fill="#fff"><circle cx="20" cy="14" r="7"/><path d="M10 26h20v14H10z"/><rect x="33" y="22" width="20" height="16" rx="2"/><rect x="6" y="42" width="48" height="5"/></svg>
    </div></div>
    <h3>Execution</h3>
    <p>99% done = ZERO% done, if it is<br>not done until it is 100% done, we<br>are pedantic about result.</p>
    <span class="more">Learn More <svg width="20" height="20" viewBox="0 0 20 20"><circle cx="10" cy="10" r="9" fill="none" stroke="#777" stroke-width="1.5"/><path d="M8 6l4 4-4 4" fill="none" stroke="#777" stroke-width="1.5"/></svg></span>
  </div>
</div>

<h2 class="section-title abs center about-title">About Aroma Forge</h2>
<p class="section-text abs center about-text" style="left:250px">Lorem Ipsum is simply dummy text of the printing and typesetting industry. Lorem Ipsum has been the industry's standard dummy text ever since the make a type specimen book.</p>
<div class="video abs" role="img" aria-label="Video still of amber perfume vials among pink blossoms and red berries"></div>
<svg class="play abs" width="72" height="72" viewBox="0 0 72 72"><circle cx="36" cy="36" r="32" fill="none" stroke="#2f8fd0" stroke-width="5"/><path d="M29 22l20 14-20 14z" fill="#2f8fd0"/></svg>

<div class="services-band abs" role="img" aria-label="Soft-focus lavender field in blue tones"></div>
<h2 class="section-title abs center services-title">Our Services</h2>
<p class="section-text abs center services-text" style="left:250px">Lorem Ipsum is simply dummy text of the printing and typesetting industry. Lorem Ipsum has been the industry's standard dummy text ever since the make a type specimen book.</p>
<article class="service-card abs" style="left:78px">
  <div class="service-photo" role="img" aria-label="Pink fragrance bottles with blossoms" style="background:radial-gradient(circle at 30% 45%,#e07aa8 0%,rgba(224,122,168,0) 35%),radial-gradient(circle at 70% 70%,#9a86c9 0%,rgba(154,134,201,0) 30%),linear-gradient(135deg,#f3e3e8,#d9a9bd 60%,#efe1e6)"></div>
  <h4>Fragrance Matching<br>Services (GCMS)</h4>
</article>
<article class="service-card abs" style="left:435px">
  <div class="service-photo" role="img" aria-label="Glass perfume bottles with dried rose petals" style="background:radial-gradient(circle at 50% 80%,#c07a7a 0%,rgba(192,122,122,0) 40%),linear-gradient(180deg,#f4f0ec,#e6d3cf 60%,#d9b3b0)"></div>
  <h4>Locally manufactured<br>FMCG fragrances</h4>
</article>
<article class="service-card abs" style="left:789px">
  <div class="service-photo" role="img" aria-label="Amber essential oil bottles with fresh herbs" style="background:radial-gradient(circle at 45% 65%,#a5602c 0%,rgba(165,96,44,0) 35%),radial-gradient(circle at 80% 30%,#5e8a3e 0%,rgba(94,138,62,0) 40%),linear-gradient(135deg,#7f9a62,#b9b39a 60%,#ddd8cc)"></div>
  <h4>Small Minimum Order<br>Quantity (10KG)</h4>
</article>
<div class="carousel-arrows abs">
  <svg width="38" height="20" viewBox="0 0 38 20"><path d="M36 10H3M11 2L3 10l8 8" fill="none" stroke="#333" stroke-width="2"/></svg>
  <svg width="38" height="20" viewBox="0 0 38 20"><path d="M2 10h33M27 2l8 8-8 8" fill="none" stroke="#2f8fd0" stroke-width="2"/></svg>
</div>

<section class="products abs">
  <h2 class="section-title abs center products-title">Our Products</h2>
  <svg class="abs" style="left:58px;top:218px" width="18" height="44" viewBox="0 0 18 44"><path d="M16 2L3 22l13 20" fill="none" stroke="#2f8fd0" stroke-width="2"/></svg>
  <svg class="abs" style="left:1122px;top:218px" width="18" height="44" viewBox="0 0 18 44"><path d="M2 2l13 20L2 42" fill="none" stroke="#222" stroke-width="2"/></svg>
  <div class="product abs" style="left:90px"><div class="product-ring"><div class="product-photo" role="img" aria-label="100G perfume oil bottle"></div></div><p>100G Perfume Oil</p></div>
  <div class="product muted abs" style="left:350px"><div class="product-ring"><div class="product-photo" role="img" aria-label="200G perfume oil bottle"></div></div><p>200G Perfume Oil</p></div>
  <div class="product abs" style="left:610px"><div class="product-ring"><div class="product-photo" role="img" aria-label="500G perfume oil bottle"></div></div><p>500G Perfume Oil</p></div>
  <div class="product abs" style="left:870px"><div class="product-ring"><div class="product-photo" role="img" aria-label="1KG perfume oil bottle"></div></div><p>1KG Perfume Oil</p></div>
</section>

<h2 class="section-title abs center news-title">Subcribe Newsletter</h2>
<p class="section-text abs center news-text" style="left:250px">Lorem Ipsum is simply dummy text of the printing and typesetting industry. Lorem Ipsum has been the industry's standard dummy text ever since the make a type specimen book.</p>
<div class="subscribe abs">
  <div class="subscribe-field">
    <svg width="22" height="16" viewBox="0 0 22 16"><rect x="1" y="1" width="20" height="14" fill="#2f8fd0"/><path d="M1 1l10 8 10-8" fill="none" stroke="#fff" stroke-width="1.5"/></svg>
    Enter Your Email...
  </div>
  <span class="btn subscribe-btn">Subscribe</span>
</div>

<footer class="site-footer abs">
  <h3 class="footer-title abs">Get In Touch</h3>
  <div class="contact-line abs" style="top:112px">
    <svg width="14" height="20" viewBox="0 0 14 20"><path d="M7 1a6 6 0 0 1 6 6c0 5-6 12-6 12S1 12 1 7a6 6 0 0 1 6-6z" fill="#2f8fd0"/><circle cx="7" cy="7" r="2.3" fill="#343434"/></svg>
    <span>Unit 4, 22 Juniper Lane, Cedar<br>Park, Riverbend 2190</span>
  </div>
  <div class="contact-line abs" style="top:177px">
    <svg width="16" height="16" viewBox="0 0 16 16"><path d="M3 1l3 3-2 2c1 2 3 4 5 5l2-2 3 3-2 3C7 14 2 9 1 3z" fill="#2f8fd0"/></svg>
    <span>+27(0) 11 555 0147</span>
  </div>
  <div class="contact-line abs" style="top:227px">
    <svg width="18" height="14" viewBox="0 0 18 14"><rect x="0" y="0" width="18" height="14" fill="#2f8fd0"/><path d="M0 0l9 7 9-7" fill="none" stroke="#343434" stroke-width="1.5"/></svg>
    <span>hello@aromaforge.example</span>
  </div>
  <div class="social abs" style="top:282px"><span></span><span></span><span></span></div>
  <div class="field abs" style="left:435px;top:108px;width:320px">Name Here*</div>
  <div class="field abs" style="left:791px;top:108px;width:331px">Email Here*</div>
  <div class="field abs" style="left:435px;top:192px;width:687px">Message Here*</div>
  <span class="btn send-btn abs">Send Message</span>
</footer>
<div class="footer-bar abs">Copyright © <b>AROMA FORGE MASTER PERFUMERS</b> - 2018 . All Right Reserved</div>

</body>
</html>
```